Harbourline Plumbing business card full re design & logo design

Harbourline Plumbing is a Sydney based mechanical plumbing contractor company.
We would like a full redesign with new logo etc which we can take to a future website, uniforms, vehicle sign writing etc.
Blue is my preferred choice of colour but i would be open to see a couple of alternatives thrown in the mix to see how they compare. I am open to see on white cards, black cards etc. Open to many new ideas.
Please see attached original business cards which have been used for the last 5 years.

Target Market(s)

Mechanical services industry.

Industry/Entity Type

Plumbing

Contact Information for Business Card

Colin Ashdale
Director

Mob: 0427 590 614
Email: colin@harbourlineplumbing.net.au
PO BOX 816
Merrowdale NSW 2159
Lic: 583106k

Logo Text

Harbourline Plumbing

Font styles to use
Sans Serif

Colors
0655a3
3276b5
0792cd
33a6d7
85cae6
000000
333333
474747

Requirements
Must have
• Things that make it very professional and very well presented.
Nice to have
• Same description or very similar to attached uploaded file
Should not have
• Anything that makes it look unprofessional or cartoony.

```html
<!DOCTYPE html>
<html lang="en">
<head>
<meta charset="utf-8">
<title>Harbourline Plumbing – Business Card</title>
<link rel="stylesheet" href="https://fonts.googleapis.com/css2?family=Work+Sans:ital,wght@0,300;0,400;0,500;0,600;0,700;1,700&display=swap">
<style>
  :root {
    --blue-deep: #0655a3;
    --blue-mid: #3276b5;
    --blue-bright: #0792cd;
    --blue-sky: #33a6d7;
    --blue-pale: #85cae6;
    --ink: #333333;
    --ink-soft: #474747;
    --paper: #ffffff;
    --stage: #2b2b2b;
  }
  * { box-sizing: border-box; margin: 0; padding: 0; }
  html, body { width: 1200px; height: 900px; overflow: hidden; }
  body {
    background: var(--stage);
    font-family: "Work Sans", Arial, sans-serif;
    display: flex;
    flex-direction: column;
    align-items: center;
    justify-content: center;
    gap: 56px;
  }
  .card {
    width: 560px;
    height: 320px;
    position: relative;
    overflow: hidden;
    box-shadow: 0 14px 30px rgba(0,0,0,.45);
  }

  /* Front */
  .card-front {
    background: linear-gradient(135deg, #0a5cb8 0%, var(--blue-deep) 100%);
    color: var(--paper);
    text-align: center;
    padding-top: 46px;
  }
  .brand {
    display: inline-flex;
    align-items: center;
    gap: 10px;
    font-weight: 700;
    font-size: 34px;
    letter-spacing: .5px;
    text-transform: uppercase;
  }
  .brand-dot {
    width: 14px; height: 14px; border-radius: 50%;
    background: currentColor;
  }
  .card-front .services-title {
    margin-top: 34px;
    font-weight: 600;
    font-size: 19px;
    letter-spacing: .6px;
  }
  .card-front .specialising {
    margin-top: 8px;
    font-weight: 600;
    font-size: 16px;
    letter-spacing: .5px;
  }
  .card-front .service-list {
    margin-top: 14px;
    font-weight: 400;
    font-size: 14px;
    line-height: 1.5;
    letter-spacing: .3px;
  }
  .card-front .tagline {
    margin-top: 14px;
    font-weight: 700;
    font-style: italic;
    font-size: 14px;
  }

  /* Back */
  .card-back { background: var(--paper); }
  .card-back .brand {
    position: absolute;
    top: 44px; right: 34px;
    color: var(--blue-deep);
    font-size: 26px;
  }
  .card-back .brand-dot { width: 11px; height: 11px; }
  .person {
    position: absolute;
    left: 0; top: 118px;
    padding-left: 38px;
  }
  .person-marker {
    position: absolute;
    left: 0; top: 2px;
    width: 14px; height: 44px;
    background: var(--blue-deep);
  }
  .person-name {
    color: var(--blue-deep);
    font-weight: 500;
    font-size: 25px;
    letter-spacing: 1.5px;
    text-transform: uppercase;
  }
  .person-role {
    color: var(--ink-soft);
    font-weight: 300;
    font-size: 15px;
    letter-spacing: .6px;
    margin-top: 2px;
  }
  .rule {
    position: absolute;
    left: 0; right: 0; top: 182px;
    height: 3px;
    background: var(--blue-deep);
  }
  .band {
    position: absolute;
    left: 0; right: 0; bottom: 0;
    height: 128px;
    background: linear-gradient(135deg, #0a5cb8 0%, var(--blue-deep) 100%);
    color: var(--paper);
  }
  .contact {
    position: absolute;
    left: 38px; bottom: 22px;
    font-size: 14px;
    line-height: 1.4;
    font-weight: 300;
    list-style: none;
  }
  .contact b { font-weight: 600; }
  .address {
    position: absolute;
    right: 34px; top: 16px;
    text-align: right;
    font-size: 14px;
    font-weight: 300;
    line-height: 1.35;
  }
  .address-company { font-weight: 600; letter-spacing: .4px; }
</style>
</head>
<body>

  <section class="card card-front" aria-label="Business card front">
    <div class="brand"><span class="brand-dot"></span>Harbourline Plumbing</div>
    <h2 class="services-title">MECHANICAL PLUMBING SERVICES</h2>
    <p class="specialising">SPECIALISING IN:</p>
    <p class="service-list">
      Make Good | Refurbishment | Tenancy | Fit Out<br>
      Plant Room Works | Shut Downs | Change Overs
    </p>
    <p class="tagline">HARBOURLINE have the SOLUTION</p>
  </section>

  <section class="card card-back" aria-label="Business card back">
    <div class="brand"><span class="brand-dot"></span>Harbourline Plumbing</div>
    <div class="person">
      <span class="person-marker"></span>
      <h1 class="person-name">Colin Ashdale</h1>
      <p class="person-role">Director</p>
    </div>
    <div class="rule"></div>
    <div class="band">
      <address class="address" style="font-style:normal">
        <div class="address-company">HARBOURLINE PLUMBING</div>
        <div>P. O. Box 816</div>
        <div>Merrowdale NSW 2159</div>
      </address>
      <ul class="contact">
        <li><b>Mobile:</b> 0427 590 614</li>
        <li><b>Email:</b> colin@harbourlineplumbing.net.au</li>
        <li><b>Lic:</b> 583106k</li>
      </ul>
    </div>
  </section>

</body>
</html>
```